Menu Edit

Hello. We need a pricing edit on our current menu and new logo swapped (we already have the new logo), as well as colour changes. Also, we require a takeaway menu, in-store menu and footpath a-frame edit as well. I have attached the files bellow.

```html
<!DOCTYPE html>
<html lang="en">
<head>
<meta charset="utf-8">
<title>Tide &amp; Table Fish Grill – Menu Suite</title>
<link href="https://fonts.googleapis.com/css2?family=Roboto+Slab:wght@500;600&family=Montserrat:ital,wght@0,400;0,500;0,600;0,700;1,500&display=swap" rel="stylesheet">
<style>
:root{
  --ink:#231f20;
  --red:#ee4123;
  --white:#ffffff;
  --rule:#5a5657;
  --soft:#d9d9d9;
  --page:#ffffff;
  --slab:"Roboto Slab", Georgia, serif;
  --sans:"Montserrat", Arial, sans-serif;
}
*{margin:0;padding:0;box-sizing:border-box}
html,body{width:1200px;height:2621px;overflow:hidden;background:var(--page)}
body{position:relative;font-family:var(--sans);color:var(--white)}
.panel{position:absolute;background:var(--ink);box-shadow:6px 6px 8px rgba(0,0,0,.35);overflow:hidden}
.poster{width:468px;height:694px;top:108px}
.poster--hours{left:94px}
.poster--platters{left:620px}
.cover{left:238px;top:844px;width:694px;height:524px}
.spread{left:238px;width:694px;height:524px}
.spread--one{top:1402px}
.spread--two{top:1958px}
.t{position:absolute;white-space:nowrap}
.c{left:0;right:0;text-align:center}
.red{color:var(--red)}
.art{position:absolute;background:radial-gradient(circle at 40% 40%,rgba(238,65,35,.55),rgba(238,65,35,.15) 45%,rgba(35,31,32,0) 72%)}
.hatch{position:absolute;background:radial-gradient(circle,rgba(238,65,35,.7),rgba(238,65,35,0) 70%)}
.brand{font-family:var(--sans);font-weight:600;color:var(--white);letter-spacing:.02em}
.brand-dot{display:inline-block;width:.5em;height:.5em;border:2px solid var(--white);border-radius:50%;margin-left:.35em;vertical-align:middle}

/* posters */
.poster-title{font-family:var(--slab);font-weight:600;font-size:38px;line-height:44px}
.hours{font-size:20px;line-height:24px;font-weight:500}
.hours b{color:var(--red);font-weight:700;margin-right:12px}
.services{font-size:21px;line-height:26px;letter-spacing:.04em;text-transform:uppercase}
.services .bar{color:var(--red)}
.byo{font-size:13.5px;font-weight:700;line-height:18px}
.red-rule{position:absolute;left:37px;width:394px;height:3px;background:var(--red)}
.prep-label{font-size:16px;line-height:20px;font-weight:500}
.prep-options{font-size:14px;line-height:18px;font-weight:500;letter-spacing:.02em}
.phone{font-size:48px;line-height:54px;font-weight:700;letter-spacing:.02em}
.phone svg{width:44px;height:38px;vertical-align:-3px;margin-right:10px}
.web-pill{position:absolute;left:66px;width:336px;top:622px;height:32px;border-radius:6px;background:var(--red);font-size:20px;font-weight:700;line-height:32px;text-align:center}
.platter-title{font-family:var(--slab);font-weight:500;font-size:30px;line-height:36px}
.short-rule{position:absolute;left:216px;width:36px;height:3px;background:var(--red)}
.platter-list{position:absolute;left:44px;width:379px;top:292px;list-style:none}
.platter-list li{height:33px;border-bottom:1px solid var(--soft);font-size:17px;font-weight:700;text-align:center;line-height:33px}
.includes-head{font-size:15px;font-weight:700;line-height:20px}
.includes{position:absolute;left:50px;width:368px;top:436px;font-size:15px;line-height:20px;text-align:center}

/* menu spreads */
.sec-title{font-family:var(--slab);font-weight:500;font-size:20px;line-height:26px}
.sec-title::after{content:"";display:block;width:16px;height:2px;background:var(--red);margin-top:1px}
.menu-list{position:absolute;list-style:none}
.menu-list li{display:flex;justify-content:space-between;font-size:8px;font-weight:700;border-bottom:1px solid var(--rule)}
.menu-list li:last-child{border-bottom:none}
.menu-list small{font-size:6px;font-weight:500}
.menu-list .price{color:var(--red);font-weight:500;letter-spacing:.12em}
.note{font-size:8px;line-height:12px}
.feature-box{position:absolute;left:359px;top:23px;width:289px;height:257px;border:1px solid var(--soft)}
.feature{position:absolute;left:10px;right:10px}
.feature-head{display:flex;justify-content:space-between;font-size:8px;font-weight:700;line-height:12px}
.feature-head small{font-size:6px;font-weight:500}
.feature-head .price{color:var(--red);font-weight:500;letter-spacing:.12em}
.feature p{font-size:8px;line-height:12px;margin-top:3px}
.info-box{position:absolute;left:359px;top:351px;width:288px;height:138px;border-radius:4px;background:var(--red);text-align:center;font-size:10px;font-weight:700;padding-top:7px}
.info-box p{line-height:15.5px}
.info-box p+p{margin-top:4px}
.fish-box{position:absolute;left:45px;top:24px;width:290px;height:248px;border:3px double var(--soft)}
.source-box{position:absolute;left:46px;top:288px;width:288px;height:53px;border-radius:4px;background:var(--red);font-size:8px;font-style:italic;font-weight:500;line-height:12px;padding:7px 18px 0}
.salad{position:absolute;left:359px;width:288px}
.salad h4{font-size:8px;font-weight:700;color:var(--red);line-height:12px}
.salad p{font-size:8px;line-height:13.5px;margin-top:2px}
</style>
</head>
<body>

<!-- Footpath A-frame: opening hours -->
<section class="panel poster poster--hours">
  <div class="art" role="img" aria-label="Illustration of a plate with grill-marked fish, knife and fork" style="left:-10px;top:-10px;width:330px;height:235px"></div>
  <div class="hatch" role="img" aria-label="Small grill-mark decoration" style="left:360px;top:85px;width:62px;height:44px"></div>
  <div class="t brand" style="right:44px;top:133px;font-size:15px">TIDE &amp; TABLE FISH GRILL</div>
  <h1 class="t c poster-title" style="top:230px">Open Every Day</h1>
  <p class="t c hours" style="top:280px"><b>Mon – Thurs</b>5pm to 9pm</p>
  <p class="t c hours" style="top:305px"><b>Fri – Sun</b>12pm to 9pm</p>
  <p class="t c services" style="top:349px">Casual Dining <span class="bar">|</span> Takeaway</p>
  <p class="t c services" style="top:376px">Online Ordering &amp; Delivery</p>
  <p class="t c services" style="top:402px">Fresh Retail</p>
  <p class="t c byo" style="top:436px">BYO Welcome! Wine, Beer &amp; Spirits / Soft Drinks Available</p>
  <div class="red-rule" style="top:464px"></div>
  <p class="t c prep-label" style="top:472px">Choose your preparation:</p>
  <p class="t c prep-options" style="top:496px">PANKO CRUMBED / TEMPURA BATTERED / GRILLED</p>
  <div class="red-rule" style="top:520px"></div>
  <p class="t c phone" style="top:552px"><svg viewBox="0 0 44 38" aria-hidden="true"><path fill="#fff" d="M2 12c0-6 8-10 20-10s20 4 20 10v3h-10v-4c-3-1-7-1-10-1s-7 0-10 1v4H2z"/><path fill="#fff" d="M9 16h26l5 10v10H4V26z"/><g fill="#231f20"><rect x="13" y="22" width="4" height="3"/><rect x="20" y="22" width="4" height="3"/><rect x="27" y="22" width="4" height="3"/><rect x="13" y="27" width="4" height="3"/><rect x="20" y="27" width="4" height="3"/><rect x="27" y="27" width="4" height="3"/></g></svg>3901 4426</p>
  <div class="web-pill">www.tideandtable.com.au</div>
</section>

<!-- Footpath A-frame: cooked seafood platters -->
<section class="panel poster poster--platters">
  <div class="art" role="img" aria-label="Illustration of a plate with grill-marked fish, knife and fork" style="left:-10px;top:-10px;width:330px;height:235px"></div>
  <div class="hatch" role="img" aria-label="Small grill-mark decoration" style="left:360px;top:85px;width:62px;height:44px"></div>
  <div class="t brand" style="right:44px;top:133px;font-size:15px">TIDE &amp; TABLE FISH GRILL</div>
  <h1 class="t c platter-title" style="top:234px">Cooked Seafood Platters</h1>
  <div class="short-rule" style="top:273px"></div>
  <ul class="platter-list">
    <li>Cooked Platter for One</li>
    <li>Cooked Platter for Two</li>
    <li>Cooked Platter for Three</li>
  </ul>
  <p class="t c includes-head red" style="top:412px">Cooked Seafood Platters include:</p>
  <p class="includes">Queensland whiting, calamari, salt &amp; pepper calamari, ocean king prawns, sea scallops, beer battered chips, one of our freshly made salads, homemade tartare sauce, lemon &amp; parsley.</p>
  <p class="t c phone" style="top:552px"><svg viewBox="0 0 44 38" aria-hidden="true"><path fill="#fff" d="M2 12c0-6 8-10 20-10s20 4 20 10v3h-10v-4c-3-1-7-1-10-1s-7 0-10 1v4H2z"/><path fill="#fff" d="M9 16h26l5 10v10H4V26z"/><g fill="#231f20"><rect x="13" y="22" width="4" height="3"/><rect x="20" y="22" width="4" height="3"/><rect x="27" y="22" width="4" height="3"/><rect x="13" y="27" width="4" height="3"/><rect x="20" y="27" width="4" height="3"/><rect x="27" y="27" width="4" height="3"/></g></svg>3901 4426</p>
  <div class="web-pill">www.tideandtable.com.au</div>
</section>

<!-- Takeaway menu: cover -->
<section class="panel cover">
  <div class="art" role="img" aria-label="Large illustration of a plate with grill-marked fish, knife and fork" style="left:40px;top:-20px;width:560px;height:420px"></div>
  <div class="hatch" role="img" aria-label="Grill-mark decoration" style="left:440px;top:345px;width:120px;height:92px"></div>
  <div class="t brand c" style="top:440px;font-size:34px;line-height:42px">TIDE &amp; TABLE FISH GRILL</div>
</section>

<!-- Takeaway menu: inside spread one -->
<section class="panel spread spread--one">
  <h2 class="t sec-title" style="left:46px;top:34px">Chips</h2>
  <ul class="menu-list" style="left:46px;width:289px;top:69px">
    <li style="height:17px;line-height:17px"><span>Beer Battered Chips</span><span class="price">5</span></li>
    <li style="height:17px;line-height:17px"><span>Classic Chips <small>GF</small></span><span class="price">5</span></li>
    <li style="height:17px;line-height:17px"><span>Sweet Potato Chips <small>GF</small></span><span class="price">5</span></li>
    <li style="height:17px;line-height:17px"><span>Greek style chips with feta &amp; wild oregano</span><span class="price">7</span></li>
  </ul>

  <h2 class="t sec-title" style="left:46px;top:173px">Starters &amp; Sides</h2>
  <ul class="menu-list" style="left:46px;width:289px;top:206px">
    <li style="height:18px;line-height:18px"><span>Crumbed Calamari (8)</span><span class="price">8</span></li>
    <li style="height:18px;line-height:18px"><span>Salt &amp; Pepper Calamari (8)</span><span class="price">9</span></li>
    <li style="height:18px;line-height:18px"><span>Potato Scallop</span><span class="price">2</span></li>
    <li style="height:18px;line-height:18px"><span>Crumbed Ocean King Prawn Cutlets (2)</span><span class="price">9</span></li>
    <li style="height:18px;line-height:18px"><span>Crumbed Sea Scallops (2)</span><span class="price">7</span></li>
    <li style="height:18px;line-height:18px"><span>BBQ Prawn Skewer</span><span class="price">9</span></li>
    <li style="height:18px;line-height:18px"><span>Grilled Halloumi (3)</span><span class="price">10</span></li>
  </ul>

  <h2 class="t sec-title" style="left:46px;top:369px">Kid's Fish &amp; Chips</h2>
  <p class="t note" style="left:46px;top:404px">Served with sauce.</p>
  <ul class="menu-list" style="left:46px;width:289px;top:423px">
    <li style="height:18px;line-height:18px"><span>Crumbed Cod Bites <small>with chips</small></span><span class="price">9</span></li>
    <li style="height:18px;line-height:18px"><span>Crumbed Calamari (4) <small>with chips</small></span><span class="price">9</span></li>
    <li style="height:18px;line-height:18px"><span>Real Chicken Nuggets <small>with chips</small></span><span class="price">9</span></li>
  </ul>
  <div class="hatch" role="img" aria-label="Grill-mark decoration" style="left:-4px;top:468px;width:64px;height:60px"></div>

  <div class="feature-box">
    <h2 class="t sec-title" style="left:10px;top:10px">Something Different</h2>
    <div class="feature" style="top:47px">
      <div class="feature-head"><span>Fish Burger <small>with chips</small></span><span class="price">13.9</span></div>
      <p>Crumbed cod fillet, lettuce, tomato &amp; homemade tartare sauce in a sesame bun.</p>
    </div>
    <div class="feature" style="top:98px">
      <div class="feature-head"><span>Fish Tacos (3) <small>with chips</small></span><span class="price">13.9</span></div>
      <p>Tempura battered cod, shredded cabbage, smokey chipotle mayonnaise &amp; coriander in soft flour tortillas.</p>
    </div>
    <div class="feature" style="top:149px">
      <div class="feature-head"><span>Grilled Chicken Burger <small>with chips</small></span><span class="price">14.9</span></div>
      <p>Grilled chicken breast, cheddar cheese, lettuce, tomato, fresh avocado &amp; aioli in a sesame bun.</p>
    </div>
    <div class="feature" style="top:200px">
      <div class="feature-head"><span>Grilled Steak Burger <small>with chips</small></span><span class="price">13.9</span></div>
      <p>Tender “grass fed” rib fillet, caramelised onion, Swiss cheese, lettuce &amp; tomato with whiskey BBQ sauce in a sesame bun.</p>
    </div>
  </div>

  <h2 class="t sec-title" style="left:359px;top:290px">Sauces</h2>
  <ul class="menu-list" style="left:359px;width:289px;top:323px">
    <li style="height:17px;line-height:17px"><span>Homemade Tartare, Aioli, Tomato &amp; Sweet Chilli</span><span class="price">1</span></li>
  </ul>

  <div class="info-box">
    <p>Our seafood is deep-fried to golden goodness<br>with premium 100% Australian grown and<br>pressed canola oil.</p>
    <p>Gluten friendly options are available.</p>
    <p>Our takeaway packaging is eco friendly.</p>
    <p>Public Holiday surcharge 15%.</p>
    <p>Menu substitutions are not available.</p>
  </div>
</section>

<!-- Takeaway menu: inside spread two -->
<section class="panel spread spread--two">
  <div class="fish-box">
    <h2 class="t sec-title" style="left:8px;top:8px">Fish &amp; Chips</h2>
    <p class="t note" style="left:8px;top:40px;white-space:normal;width:260px">Served with your choice of chips, homemade tartare sauce, lemon &amp; parsley.</p>
    <ul class="menu-list" style="left:8px;width:268px;top:66px">
      <li style="height:15.6px;line-height:15.6px"><span>Classic Cod <small>with chips</small></span><span class="price">12.9</span></li>
      <li style="height:15.6px;line-height:15.6px"><span>Crumbed Whiting (QLD) <small>with chips</small></span><span class="price">15.9</span></li>
      <li style="height:15.6px;line-height:15.6px"><span>Snapper (QLD, LC) <small>with chips</small></span><span class="price">18.9</span></li>
      <li style="height:15.6px;line-height:15.6px"><span>Ocean Barramundi (QLD, FRM) <small>with chips</small></span><span class="price">18.9</span></li>
      <li style="height:15.6px;line-height:15.6px"><span>Crispy Skin Salmon (TAS, FRM) <small>with chips</small></span><span class="price">18.9</span></li>
      <li style="height:15.6px;line-height:15.6px"><span>Crispy Skin Ocean Trout (TAS, FRM) <small>with chips</small></span><span class="price">18.9</span></li>
      <li style="height:15.6px;line-height:15.6px"><span>Crumbed Calamari (8) <small>with chips</small></span><span class="price">12.9</span></li>
      <li style="height:15.6px;line-height:15.6px"><span>Salt &amp; Pepper Calamari (8) <small>with chips</small></span><span class="price">13.9</span></li>
      <li style="height:15.6px;line-height:15.6px"><span>BBQ Prawn Skewers (2) <small>with chips</small></span><span class="price">22.9</span></li>
    </ul>
    <p class="t c note" style="top:215px;font-weight:700">Choose your preparation:</p>
    <p class="t c note" style="top:228px;font-weight:500">PANKO CRUMBED / TEMPURA BATTERED / GRILLED</p>
  </div>
  <div class="source-box">Our premium quality fish is line caught (LC) and farmed (FRM) from pristine Australian waters, delivered in-store every morning for you to enjoy market fresh!</div>

  <h2 class="t sec-title" style="left:359px;top:34px">Salads</h2>
  <p class="t note" style="left:359px;top:65px">Freshly prepared to order using the freshest local produce.</p>
  <p class="t note" style="right:47px;top:87px;text-align:right">Full / Side</p>
  <p class="t note red" style="left:610px;top:100px;word-spacing:14px">10 7</p>
  <div style="position:absolute;left:359px;top:114px;width:289px;height:1px;background:var(--rule)"></div>
  <div class="salad" style="top:117px">
    <h4>Greek</h4>
    <p>Lettuce, cucumber, tomato, red onion, Greek olives, feta, wild oregano, tossed in Greek extra virgin olive oil vinaigrette.</p>
  </div>
  <div class="salad" style="top:170px">
    <h4>Coleslaw</h4>
    <p>Red &amp; green cabbage, eschallots, carrot, tossed in a light mayonnaise dressing.</p>
  </div>
  <div class="salad" style="top:223px">
    <h4>Crunchy Asian Slaw</h4>
    <p>Red &amp; green cabbage, eschallots, carrot, coriander, crispy noodles, tossed in a light soy dressing.</p>
  </div>
  <div class="salad" style="top:276px">
    <h4>Roast Pumpkin &amp; Wild Rocket</h4>
    <p>Roast pumpkin, wild rocket, freshly shaved Parmigiano Reggiano, toasted pine nuts, tossed in Greek extra virgin olive oil &amp; vintage balsamic vinegar.</p>
  </div>
  <div class="hatch" role="img" aria-label="Grill-mark decoration" style="left:622px;top:0;width:76px;height:88px"></div>

  <h2 class="t sec-title" style="left:46px;top:357px">Cooked Seafood Platters</h2>
  <p class="t note" style="left:46px;top:387px;white-space:normal;width:602px">Cooked Seafood Platters include: Queensland whiting, calamari, salt &amp; pepper calamari, ocean king prawns, sea scallops, beer battered chips, one of our freshly made salads, homemade tartare sauce, lemon &amp; parsley.</p>
  <ul class="menu-list" style="left:46px;width:602px;top:420px">
    <li style="height:18px;line-height:18px"><span>Cooked Platter for One</span><span class="price">21.9</span></li>
    <li style="height:18px;line-height:18px"><span>Cooked Platter for Two</span><span class="price">41.9</span></li>
    <li style="height:18px;line-height:18px"><span>Cooked Platter for Three</span><span class="price">61.9</span></li>
  </ul>
  <p class="t c note" style="top:478px;font-weight:500">Our seafood platters are available panko crumbed only.</p>
</section>

</body>
</html>
```